Mobile Platform based Diabetes Management Service need flyer design

We need a flyer design for LuMaKai Service. We developed a mobile technology based platform where Diabetes patients can share their daily disease management information with their doctors and receive personalized advice. For more information, please check out www.lumakai-health.com.

We have a preliminary design for business card. and like to the flyer to go for similar style.

At this point, we are looking for framework draft only. Final wording on flyer will be in Chinese and we can insert that in later.

Target Market(s)

20 to 50 years old, smart phone users, diaganosed with Diabetes, health concisous,
full time working, busy, reluctant to schedule face to face doctor visit.

Industry/Entity Type

Business

Requirements
Must have
• The flyer should include LuMa Kai Logo. You can find the logo on the file I uploaded - the business card design file.

That being said, we also think LuMaKai logo can be a bit more flat. So please feel free to modify the logo design.
Nice to have
• We designed a "digital doctor" image - Dou Fen. You can include this cartoon figure as needed.

```html
<!DOCTYPE html>
<html lang="zh">
<head>
<meta charset="utf-8">
<title>LuMaKai 糖尿病管理服务</title>
<link href="https://fonts.googleapis.com/css2?family=Noto+Sans+SC:wght@400;500;700;900&display=swap" rel="stylesheet">
<style>
  :root {
    --lime: #8cd400;
    --lime-light: #b6ff2a;
    --lime-deep: #5e9e00;
    --ink: #1d1d1d;
    --muted: #8a8a8a;
    --paper: #ffffff;
    --device: #1c1c1c;
    --device-edge: #4a4a4a;
    --chat-bg: #f4f4f4;
    --stamp: #e2e2e2;
    --avatar-doctor: #c9a27a;
    --avatar-user: #e8b98e;
  }
  * { margin: 0; padding: 0; box-sizing: border-box; }
  html, body { width: 1200px; height: 900px; overflow: hidden; background: var(--paper); }
  body { font-family: "Noto Sans SC", sans-serif; color: var(--ink); position: relative; }

  .top-band {
    position: absolute; left: 0; top: 0; width: 1200px; height: 43px;
    background: linear-gradient(180deg, var(--lime-light) 0%, var(--lime) 100%);
  }
  .brand {
    position: absolute; left: 107px; top: 6px; height: 31px;
    display: flex; align-items: center; gap: 8px;
    color: var(--paper); font-size: 22px; font-weight: 700; letter-spacing: 0.5px;
  }
  .brand-dot { width: 18px; height: 18px; border-radius: 50%; background: var(--paper); }
  .top-rule {
    position: absolute; left: 0; top: 50px; width: 1200px; height: 13px;
    background: linear-gradient(180deg, var(--lime) 0%, var(--lime-light) 100%);
  }

  .device {
    position: absolute;
    background: linear-gradient(160deg, var(--device-edge) 0%, var(--device) 35%, #000 100%);
  }
  .screen { position: absolute; overflow: hidden; background: var(--chat-bg); }

  /* hero phone */
  .hero-device { left: 178px; top: 98px; width: 250px; height: 512px; border-radius: 44px / 52px; }
  .hero-device .screen { left: 15px; top: 80px; width: 220px; height: 380px; }
  .status-bar {
    position: absolute; left: 0; top: 0; width: 100%; height: 20px; background: #000;
    color: var(--paper); font-size: 12px; line-height: 20px; text-align: right; padding-right: 8px;
  }
  .app-header {
    position: absolute; left: 0; top: 20px; width: 100%; height: 32px;
    background: linear-gradient(180deg, var(--lime-light), var(--lime));
    color: var(--paper); font-size: 15px; font-weight: 500; text-align: center; line-height: 32px;
  }
  .hdr-btn {
    position: absolute; top: 5px; height: 22px; padding: 0 6px;
    background: var(--lime-deep); border: 1px solid #3d6a00; border-radius: 4px;
    font-size: 12px; line-height: 20px; color: var(--paper);
  }
  .hdr-btn.back { left: 6px; }
  .hdr-btn.refresh { right: 6px; }
  .stamp {
    position: absolute; left: 6px; width: 208px; height: 12px; background: var(--stamp);
    color: var(--muted); font-size: 9.5px; line-height: 12px; text-align: center;
  }
  .avatar { position: absolute; width: 40px; height: 40px; border: 1px solid #ccc; border-radius: 3px; }
  .avatar.doctor { left: 7px; background: linear-gradient(180deg, #f2e3cf, var(--avatar-doctor)); }
  .avatar.user { right: 10px; background: linear-gradient(180deg, #f5f5f5, var(--avatar-user)); }
  .bubble {
    position: absolute; font-size: 11.5px; line-height: 16px; padding: 3px 5px; border-radius: 3px;
  }
  .bubble.in { left: 55px; width: 152px; background: var(--lime); color: var(--ink); }
  .bubble.out { right: 56px; background: var(--paper); border: 1px solid #bbb; white-space: nowrap; }
  .input-bar {
    position: absolute; left: 0; bottom: 0; width: 100%; height: 38px; background: #222;
  }
  .voice { position: absolute; left: 6px; top: 9px; width: 20px; height: 20px; border-radius: 50%; background: #ddd; }
  .input-box {
    position: absolute; left: 32px; top: 8px; width: 140px; height: 22px; background: var(--paper);
    border-radius: 4px; font-size: 11.5px; line-height: 22px; color: var(--muted); padding-left: 4px;
  }
  .send {
    position: absolute; right: 6px; top: 7px; width: 36px; height: 24px; background: var(--lime);
    border-radius: 3px; color: var(--paper); font-size: 12px; line-height: 24px; text-align: center;
  }

  /* labels and copy */
  .label {
    position: absolute; background: var(--lime); color: var(--paper); font-weight: 900;
    display: flex; align-items: center; justify-content: center; white-space: nowrap;
  }
  .hero-label { left: 107px; top: 657px; width: 387px; height: 61px; font-size: 40px; letter-spacing: 2px; }
  .hero-copy { position: absolute; left: 107px; top: 733px; width: 400px; font-size: 20px; line-height: 30px; }

  .feature { position: absolute; left: 0; width: 1200px; height: 196px; }
  .feature .device { left: 714px; top: 0; width: 86px; height: 164px; border-radius: 12px / 14px; }
  .feature .screen { left: 7px; top: 22px; width: 72px; height: 118px; background: var(--paper); }
  .feature .label { left: 870px; top: 47px; width: 235px; height: 46px; font-size: 28px; letter-spacing: 1px; }
  .feature .copy { position: absolute; left: 872px; top: 108px; width: 240px; font-size: 14.5px; line-height: 21px; }
  .divider { position: absolute; left: 641px; width: 518px; height: 0; border-top: 2px dotted var(--lime); }

  /* mini screens */
  .m-status { position: absolute; left: 0; top: 0; width: 100%; height: 5px; background: #000; }
  .m-head {
    position: absolute; left: 0; top: 5px; width: 100%; height: 10px; background: var(--lime);
    color: var(--paper); font-size: 5px; line-height: 10px; text-align: center;
  }
  .m-row {
    position: absolute; left: 2px; right: 2px; height: 21px; border-bottom: 1px solid #ddd;
    font-size: 4.5px; line-height: 6px; color: #333; padding: 2px 2px 0 3px;
  }
  .m-row.short { height: 9px; line-height: 7px; padding-top: 1px; }
  .m-row::after { content: "›"; position: absolute; right: 1px; top: 1px; font-size: 6px; color: #777; }
  .m-row .sub { color: var(--muted); display: block; }
  .m-dot { display: inline-block; width: 5px; height: 5px; border-radius: 50%; background: var(--lime); vertical-align: middle; margin-right: 2px; }
  .m-nav {
    position: absolute; left: 0; bottom: 0; width: 100%; height: 8px; background: #eee;
    border-top: 1px solid var(--lime); display: flex; justify-content: space-around;
    font-size: 4px; line-height: 7px; color: #555;
  }
  .m-value {
    position: absolute; right: 4px; top: 19px; width: 26px; height: 10px; border: 1px solid #bbb;
    font-size: 6px; font-weight: 700; line-height: 8px; text-align: center;
  }
  .m-field { position: absolute; left: 3px; top: 21px; font-size: 4.5px; color: #333; }
  .m-grid { position: absolute; left: 3px; right: 3px; top: 33px; display: grid; grid-template-columns: repeat(4, 1fr); gap: 1px; }
  .m-grid span { height: 6px; border: 1px solid #ccc; background: #f4f4f4; font-size: 3.5px; line-height: 4px; text-align: center; }
</style>
</head>
<body>
  <div class="top-band"></div>
  <div class="brand"><span class="brand-dot"></span>LuMaKai</div>
  <div class="top-rule"></div>

  <div class="device hero-device">
    <div class="screen">
      <div class="status-bar">16:30</div>
      <div class="app-header"><span class="hdr-btn back">返回</span>陆医生<span class="hdr-btn refresh">刷新</span></div>
      <div class="stamp" style="top:54px">2013年09月25日 16:02:36</div>
      <div class="avatar doctor" style="top:70px" role="img" aria-label="数字医生卡通形象头像"></div>
      <p class="bubble in" style="top:68px">您好，先不要害怕。1型糖尿病是一种免疫性疾病，首先你对该病要有充分的了解和认识，然后按照医生的方案积极治疗。</p>
      <div class="stamp" style="top:178px">2013年09月25日 16:03:26</div>
      <p class="bubble out" style="top:204px">那去哪里学习，怎么学习</p>
      <div class="avatar user" style="top:196px" role="img" aria-label="用户头像"></div>
      <div class="stamp" style="top:254px">2013年09月25日 16:07:10</div>
      <div class="avatar doctor" style="top:272px" role="img" aria-label="数字医生卡通形象头像"></div>
      <p class="bubble in" style="top:270px">以后我会经常给你发送适合你的糖尿病知识，你认真学习，如有疑问可以随时问我。知己知彼，百战不殆。</p>
      <div class="input-bar">
        <span class="voice"></span>
        <span class="input-box">在此输入消息</span>
        <span class="send">发送</span>
      </div>
    </div>
  </div>
  <div class="label hero-label">随时随地咨询医生</div>
  <p class="hero-copy">随时随地与您的医生在线沟通,分享每日血糖与饮食记录,获取专属的个性化健康建议,让糖尿病管理更轻松.</p>

  <section class="feature" style="top:92px">
    <div class="device">
      <div class="screen">
        <div class="m-status"></div>
        <div class="m-head">消息</div>
        <div class="m-row" style="top:16px">陆医生<span class="sub">最近血糖控制得不错</span></div>
        <div class="m-row" style="top:38px">陆医生<span class="sub">请按时记录饮食情况</span></div>
        <div class="m-row" style="top:60px">陆医生<span class="sub">注意餐后血糖变化</span></div>
        <div class="m-row" style="top:82px">陆医生<span class="sub">本周运动量可再增加</span></div>
        <div class="m-nav"><span>首页</span><span>咨询</span><span>记录</span><span>资料</span></div>
      </div>
    </div>
    <div class="label">随时随地咨询医生</div>
    <p class="copy">随时随地与医生沟通,分享每日记录获取个性化健康建议.</p>
  </section>
  <div class="divider" style="top:274px"></div>

  <section class="feature" style="top:290px">
    <div class="device">
      <div class="screen">
        <div class="m-status"></div>
        <div class="m-head">2013年9月</div>
        <div class="m-row" style="top:17px"><span class="m-dot"></span>空腹血糖<span class="sub">血糖偏高</span></div>
        <div class="m-row" style="top:39px"><span class="m-dot"></span>午餐前血糖<span class="sub">正常</span></div>
        <div class="m-row" style="top:61px"><span class="m-dot" style="background:#c0392b"></span>胰岛素注射<span class="sub">已完成</span></div>
        <div class="m-row" style="top:83px"><span class="m-dot" style="background:#f1c40f"></span>午餐<span class="sub">已记录</span></div>
        <div class="m-nav"><span>首页</span><span>咨询</span><span>记录</span><span>资料</span></div>
      </div>
    </div>
    <div class="label">量身定做知识库</div>
    <p class="copy">根据您的病情量身推送知识,随时学习掌握健康管理方法.</p>
  </section>
  <div class="divider" style="top:471px"></div>

  <section class="feature" style="top:487px">
    <div class="device">
      <div class="screen">
        <div class="m-status"></div>
        <div class="m-head">记录血糖</div>
        <span class="m-field">血糖值</span>
        <div class="m-value">5.5</div>
        <div class="m-grid"><span>空腹</span><span>早餐后</span><span>午餐前</span><span>午餐后</span><span>晚餐前</span><span>晚餐后</span><span>睡前</span><span>随机</span></div>
        <div class="m-row short" style="top:52px">测量日期 2013-09-23</div>
        <div class="m-row short" style="top:62px">测量时间 16:32</div>
        <div class="m-row short" style="top:72px">备注</div>
      </div>
    </div>
    <div class="label">随时随地咨询医生</div>
    <p class="copy">轻松记录每日血糖数据,医生实时查看并给出专业建议.</p>
  </section>
  <div class="divider" style="top:668px"></div>

  <section class="feature" style="top:686px">
    <div class="device">
      <div class="screen">
        <div class="m-status"></div>
        <div class="m-head">记录</div>
        <div class="m-row short" style="top:16px">记录血糖</div>
        <div class="m-row short" style="top:26px">记录血压</div>
        <div class="m-row short" style="top:36px">记录用药</div>
        <div class="m-row short" style="top:46px">记录胰岛素</div>
        <div class="m-row short" style="top:56px">记录饮食</div>
        <div class="m-row short" style="top:66px">记录运动</div>
        <div class="m-row short" style="top:76px">记录体重</div>
        <div class="m-row short" style="top:86px">记录心情</div>
        <div class="m-row short" style="top:100px">提醒设置</div>
      </div>
    </div>
    <div class="label">随时随地咨询医生</div>
    <p class="copy">饮食运动用药全面记录,帮助您养成健康的生活习惯.</p>
  </section>
</body>
</html>
```